Professional Hairdresser needs powerful, clever, simple, modern business card

I need a professional, clever, powerful, bold, attractive, modern/simplistic business card.
I specialize in dimensional hair color, precision haircutting, modern classic design, and signature finishes.
I believe in advanced education, continued training with emphasis on perfect practice, and strive to be the best at what I do.
I am trained by the industry's best and have passion for what I do, I want my business card to reflect my talents, education, capabilities, signature color techniques and design and confidence.
I want to be known as reputable, bold, artistic, aware, classic yet modern, innovative, creative, dimensional, knowledgeable, and educated.
I want something bold, simple, elegant, modern, clever, and legible.
My personal style is progressive, modern, eclectic, clean with modern luxury comfort style.
I love the use of black and white, to creative visual interest and texture. I think putting black as a solid background with white bold font makes the words jump/glow to the eye. I also think a stark white background with bold black fonts looks great, maybe with a punch of red. It is simple, clean, elegant.
I have a QR code I would like to include on the card but have no idea how to make it visually pleasing or make sense.
I do not have a set logo and am not sure if this needs to be done first or if the business card should be done first.
Updates

Reason: Very difficult decision. All designers are amazing.

Reason: Difficult decisions

Reason: Need more time as yesterday was not able to work as much as possible with designers. They are all great and look forward to having time later to look at them.

Reason: Unexpected time delay.

Target Market(s)

Early 20's-mid 60's, female and male, fashion aware, people who can afford my prices, appreciate value

Industry/Entity Type

Training

Requirements
Must have
• I would like to incorporate the QR code I have if possible.
I would like to have my name and contact info.
I would like my logo (or maybe have my logo be RT in a font like listed below).
I would like the fonts to be modern, bold, clean, readable.
Fonts I have looked at are: The font used on the book called: Morvani An Age of Bright Shapes" I really love. I have looked at glyphwell.net for font and found "Georgiquas", but the designer wanted 200 euros which I just dont have at the time. Others I looked at include "Lin Libertine", Alien-Encounters-solid-regular-italic".
I love font used in the picture I included with the Tobias.Lindqvist ad.
Clean, modern, professional, legible, structured.
Nice to have
• I envision a black background with bold, modern, simple, font in white creating the effect of the words jumping off the card, visually apparent and glowing. Like a really expensive restaurant with a sign that you cant miss because the name is in bright white on black background, simple, bold, modern but not futuristic, powerful, clever, elegant, and draws the eye making it unforgetable. Perhaps layering black and white in order to where the font will be in white.
I see balance and chic.
Perhaps
Should not have
• I appreciate the trends in business design, but realize trends come and go and not sure if having something "trendy" is advisable for me. Having said that, I like creative modern design and sometimes current trends are important in design. I do like red as accent color, the primary blue color, blue on the PixelQuorum page, the masculine/florescent purple, and the neo bold yellow and the primary color shade of yellow.
I do not want clutter.
I do not want any fonts that are swirly, old-world calligraphy, script, or penmanship style.
I do not want picture of scissors, heads of old-school beauty school hair, or barber poles.

```html
<!DOCTYPE html>
<html lang="en">
<head>
<meta charset="utf-8">
<title>Rowan Tate Professional Hair – Business Card</title>
<link rel="stylesheet" href="https://fonts.googleapis.com/css2?family=Marcellus&family=Questrial&display=swap">
<style>
  :root {
    --backdrop: #d9d9d9;
    --card-black: #050505;
    --paper-white: #ffffff;
    --accent-red: #d0201c;
    --text-light: #f2f2f2;
    --text-muted: #bdbdbd;
    --ink: #111111;
  }
  * { box-sizing: border-box; margin: 0; padding: 0; }
  html, body {
    width: 1200px;
    height: 900px;
    overflow: hidden;
    background: var(--backdrop);
  }
  .sheet {
    width: 1200px;
    height: 900px;
    display: flex;
    flex-direction: column;
    align-items: center;
    justify-content: center;
    gap: 60px;
  }
  .card {
    position: relative;
    width: 640px;
    height: 366px;
    background: var(--card-black);
    overflow: hidden;
    box-shadow: 0 6px 18px rgba(0,0,0,0.25);
  }

  /* Front */
  .card-front .edge-accent {
    position: absolute;
    top: 0; right: 0;
    width: 6px;
    height: 100%;
    background: linear-gradient(to bottom, var(--accent-red), #3a0a08);
  }
  .card-front .identity {
    position: absolute;
    left: 58px;
    bottom: 58px;
  }
  .card-front .identity-name {
    font-family: "Marcellus", serif;
    font-size: 50px;
    line-height: 1;
    color: var(--text-light);
    letter-spacing: 0.5px;
    white-space: nowrap;
    text-shadow: 0 0 8px rgba(255,255,255,0.45);
  }
  .card-front .identity-rule {
    width: 100%;
    height: 2px;
    background: var(--text-muted);
    margin: 8px 0 6px;
    box-shadow: 0 0 6px rgba(255,255,255,0.35);
  }
  .card-front .identity-tagline {
    font-family: "Questrial", sans-serif;
    font-size: 12px;
    letter-spacing: 5px;
    color: var(--text-muted);
    white-space: nowrap;
  }

  /* Back */
  .card-back .name-band {
    position: absolute;
    top: 0;
    right: 36px;
    width: 330px;
    height: 150px;
    padding: 0 28px;
    background: var(--paper-white);
    display: flex;
    align-items: center;
    justify-content: center;
  }
  .card-back .name-band-text {
    font-family: "Marcellus", serif;
    font-size: 44px;
    line-height: 1;
    color: var(--ink);
    letter-spacing: 1px;
    white-space: nowrap;
  }
  .card-back .contact-list {
    position: absolute;
    left: 40px;
    bottom: 40px;
    list-style: none;
    display: flex;
    flex-direction: column;
    gap: 12px;
  }
  .card-back .contact-item {
    display: flex;
    align-items: center;
    gap: 16px;
    font-family: "Questrial", sans-serif;
    font-size: 19px;
    color: var(--text-light);
    white-space: nowrap;
  }
  .card-back .contact-icon {
    width: 22px;
    height: 22px;
    flex: none;
  }
</style>
</head>
<body>
<main class="sheet">

  <section class="card card-front" aria-label="Card front">
    <div class="edge-accent"></div>
    <div class="identity">
      <div class="identity-name">Rowan Tate</div>
      <div class="identity-rule"></div>
      <div class="identity-tagline">PROFESSIONAL HAIR</div>
    </div>
  </section>

  <section class="card card-back" aria-label="Card back">
    <div class="name-band">
      <span class="name-band-text">Rowan Tate</span>
    </div>
    <ul class="contact-list">
      <li class="contact-item">
        <svg class="contact-icon" viewBox="0 0 24 24" aria-hidden="true">
          <circle cx="12" cy="12" r="10.5" fill="none" stroke="#d0201c" stroke-width="1.6"/>
          <path d="M8.2 7.2l2 1.8-1 1.6c.8 1.6 2 2.8 3.6 3.6l1.6-1 1.8 2-1.4 1.6c-3.8-.6-7.2-4-7.8-7.8z" fill="#d0201c"/>
        </svg>
        <span>555 014 2271</span>
      </li>
      <li class="contact-item">
        <svg class="contact-icon" viewBox="0 0 24 24" aria-hidden="true">
          <circle cx="12" cy="12" r="10.5" fill="none" stroke="#d0201c" stroke-width="1.6"/>
          <rect x="6.5" y="8" width="11" height="8" fill="none" stroke="#d0201c" stroke-width="1.4"/>
          <path d="M6.5 8l5.5 4.5 5.5-4.5" fill="none" stroke="#d0201c" stroke-width="1.4"/>
        </svg>
        <span>rowan@rowantatepro.com</span>
      </li>
      <li class="contact-item">
        <svg class="contact-icon" viewBox="0 0 24 24" aria-hidden="true">
          <circle cx="12" cy="12" r="10.5" fill="#d0201c"/>
          <circle cx="12" cy="12" r="6" fill="none" stroke="#050505" stroke-width="1.2"/>
          <ellipse cx="12" cy="12" rx="2.6" ry="6" fill="none" stroke="#050505" stroke-width="1.2"/>
          <path d="M6 12h12" stroke="#050505" stroke-width="1.2"/>
        </svg>
        <span>www.rowantatepro.com</span>
      </li>
    </ul>
  </section>

</main>
</body>
</html>
```